Proposal Template Design

We are looking to have our proposal templates redesigned. attached are examples of what we have been using. as well as our current logo

```html
<!DOCTYPE html>
<html lang="en">
<head>
<meta charset="utf-8">
<title>Proposal Template – Summit Shield Insulation</title>
<link rel="stylesheet" href="https://fonts.googleapis.com/css2?family=Fira+Sans+Condensed:wght@500;600&family=Open+Sans:wght@400;700&display=swap">
<style>
  :root {
    --backdrop: #a3a4a7;
    --paper: #ffffff;
    --navy: #06112b;
    --royal: #0a4a9a;
    --bright: #1aa7e6;
    --headline: #1f5fa9;
    --band: #1e5aa3;
    --ink: #2b2b2b;
    --nav-ink: #111111;
  }
  * { margin: 0; padding: 0; box-sizing: border-box; }
  html, body { width: 1200px; height: 960px; overflow: hidden; }
  body { background: var(--backdrop); position: relative; font-family: "Open Sans", Arial, sans-serif; color: var(--ink); }

  .page { position: absolute; top: 111px; width: 570px; height: 738px; background: var(--paper); overflow: hidden; box-shadow: 0 1px 3px rgba(0,0,0,.25); }
  .page--cover { left: 20px; }
  .page--body { left: 610px; }

  .masthead { position: absolute; left: 0; top: 0; width: 570px; height: 120px; border-bottom: 1px solid var(--bright); }
  .masthead__art { position: absolute; inset: 0; }
  .brand { position: absolute; left: 37px; top: 42px; display: flex; align-items: center; gap: 7px;
    font-family: "Fira Sans Condensed", "Arial Narrow", sans-serif; font-weight: 600; font-size: 17px; color: var(--navy); letter-spacing: .1px; }
  .brand__mark { width: 12px; height: 12px; background: var(--navy); }
  .contact { position: absolute; left: 357px; top: 19px; list-style: none; font-family: "Fira Sans Condensed", "Arial Narrow", sans-serif; font-weight: 500; font-size: 10.5px; color: #f0f4fa; }
  .contact li { display: flex; align-items: center; gap: 8px; height: 15px; }
  .contact svg { width: 8px; height: 8px; flex: none; }
  .services { position: absolute; left: 310px; top: 96px; font-family: "Fira Sans Condensed", "Arial Narrow", sans-serif; font-weight: 600; font-size: 10.5px; color: var(--nav-ink); letter-spacing: .1px; white-space: nowrap; }
  .services .sep { color: var(--bright); margin: 0 5px; font-weight: 500; }

  .hero { position: absolute; left: 0; top: 121px; width: 570px; height: 281px;
    background: linear-gradient(120deg, #d8d6cf 0%, #ebe7d9 35%, #f2eedd 55%, #8a7e6c 78%, #4a4037 100%); }

  .content { position: absolute; left: 40px; right: 40px; }
  .headline { font-family: "Fira Sans Condensed", "Arial Narrow", sans-serif; font-weight: 600; font-size: 22px; color: var(--headline); margin-bottom: 14px; }
  .content p { font-size: 11px; line-height: 17.5px; margin-bottom: 10.5px; }
  .page--cover .content { top: 421px; }

  .page--body .content { top: 143px; height: 560px; column-count: 2; column-gap: 20px; column-fill: auto; }
  .subhead { font-size: 13px; font-weight: 700; color: #111; margin-bottom: 5px; }

  .footer-band { position: absolute; left: 0; bottom: 2px; width: 570px; height: 12px; background: var(--band); }
</style>
</head>
<body>

<!-- Page 1: cover -->
<section class="page page--cover">
  <header class="masthead">
    <svg class="masthead__art" viewBox="0 0 570 120" width="570" height="120" aria-hidden="true">
      <defs>
        <linearGradient id="panelA" x1="0" y1="0" x2="1" y2="0">
          <stop offset="0" stop-color="#0a5fb8"/>
          <stop offset=".45" stop-color="#073f87"/>
          <stop offset="1" stop-color="#040c22"/>
        </linearGradient>
        <linearGradient id="barA" x1="0" y1="0" x2="1" y2="0">
          <stop offset="0" stop-color="#1cb2ec"/>
          <stop offset="1" stop-color="#0b5fb6"/>
        </linearGradient>
      </defs>
      <polygon points="220,0 570,0 570,91 290,91 278,120 240,120 260,70" fill="url(#panelA)"/>
      <polygon points="220,0 262,62 240,120 260,70" fill="#0b57ad"/>
      <polygon points="262,62 290,91 278,120 240,120" fill="#0d6cc6"/>
      <polygon points="37,95 240,95 236,108 37,108" fill="url(#barA)"/>
    </svg>
    <div class="brand"><span class="brand__mark"></span>Summit Shield Insulation</div>
    <ul class="contact">
      <li><svg viewBox="0 0 10 10"><circle cx="5" cy="5" r="4.5" fill="#fff" opacity=".8"/><circle cx="5" cy="4.2" r="1.6" fill="#0a3d80"/></svg>P.O Box 210, Ridgeford Texas 75400</li>
      <li><svg viewBox="0 0 10 10"><circle cx="5" cy="5" r="4.5" fill="#fff" opacity=".8"/><path d="M3 3 L4.2 3 L4.6 4.4 L4 5 Q5 6.5 6 6.2 L6.6 5.6 L7.6 6.2 L7.4 7.4 Q4 7.6 3 3Z" fill="#0a3d80"/></svg>555-014-2290</li>
      <li><svg viewBox="0 0 10 10"><circle cx="5" cy="5" r="4.5" fill="#fff" opacity=".8"/><rect x="2.6" y="3.4" width="4.8" height="3.4" fill="#0a3d80"/></svg>office@summitshield.example</li>
      <li><svg viewBox="0 0 10 10"><circle cx="5" cy="5" r="4.5" fill="#fff" opacity=".8"/><path d="M1 5 H9 M5 1 V9" stroke="#0a3d80" stroke-width=".8"/></svg>summitshieldinsulation.example</li>
    </ul>
    <nav class="services">SPRAY FOAM<span class="sep">|</span>FIBERGLASS<span class="sep">|</span>INSULATION<span class="sep">|</span>ROOFING</nav>
  </header>

  <div class="hero" role="img" aria-label="Photo of an installer in a white protective suit spraying foam insulation onto attic rafters"></div>

  <article class="content">
    <h1 class="headline">Tittle Headline Loremipsumdolor</h1>
    <p>Lorem ipsum dolor sit amet, consectetur adipiscing elit. Praesent ut lobortis est, at laoreet leo. Aliquam posuere placerat elementum. Pellentesque et ornare risus. Vestibulum blandit arcu nisi, elementum blandit elit facilisis a. Duis molestie malesuada condimentum. Proin auctor blandit diam vestibulum dapibus. Proin laoreet pellentesque felis, at fermentum neque sagittis ut. Duis gravida est vitae purus mollis laoreet.</p>
    <p>Pellentesque sagittis auctor sapien, vel rhoncus libero commodo et. Nullam in imperdiet ligula, eu mollis erat. In hac habitasse platea dictumst. Aliquam ligula mi, posuere vitae sem ut, vestibulum commodo dui. Integer commodo, metus vehicula laoreet interdum, odio felis condimentum metus, in pretium sem risus quis arcu. In eget nisl tempus arcu scelerisque pulvinar et sit amet magna. Lorem ipsum dolor sit amet, consectetur adipiscing elit. Praesent turpis neque, tincidunt vel ante vel, pellentesque porttitor dui. Maecenas pellentesque commodo elit et iaculis.</p>
  </article>

  <div class="footer-band"></div>
</section>

<!-- Page 2: body copy -->
<section class="page page--body">
  <header class="masthead">
    <svg class="masthead__art" viewBox="0 0 570 120" width="570" height="120" aria-hidden="true">
      <defs>
        <linearGradient id="panelB" x1="0" y1="0" x2="1" y2="0">
          <stop offset="0" stop-color="#0a5fb8"/>
          <stop offset=".45" stop-color="#073f87"/>
          <stop offset="1" stop-color="#040c22"/>
        </linearGradient>
        <linearGradient id="barB" x1="0" y1="0" x2="1" y2="0">
          <stop offset="0" stop-color="#1cb2ec"/>
          <stop offset="1" stop-color="#0b5fb6"/>
        </linearGradient>
      </defs>
      <polygon points="220,0 570,0 570,91 290,91 278,120 240,120 260,70" fill="url(#panelB)"/>
      <polygon points="220,0 262,62 240,120 260,70" fill="#0b57ad"/>
      <polygon points="262,62 290,91 278,120 240,120" fill="#0d6cc6"/>
      <polygon points="37,95 240,95 236,108 37,108" fill="url(#barB)"/>
    </svg>
    <div class="brand"><span class="brand__mark"></span>Summit Shield Insulation</div>
    <ul class="contact">
      <li><svg viewBox="0 0 10 10"><circle cx="5" cy="5" r="4.5" fill="#fff" opacity=".8"/><circle cx="5" cy="4.2" r="1.6" fill="#0a3d80"/></svg>P.O Box 210, Ridgeford Texas 75400</li>
      <li><svg viewBox="0 0 10 10"><circle cx="5" cy="5" r="4.5" fill="#fff" opacity=".8"/><path d="M3 3 L4.2 3 L4.6 4.4 L4 5 Q5 6.5 6 6.2 L6.6 5.6 L7.6 6.2 L7.4 7.4 Q4 7.6 3 3Z" fill="#0a3d80"/></svg>555-014-2290</li>
      <li><svg viewBox="0 0 10 10"><circle cx="5" cy="5" r="4.5" fill="#fff" opacity=".8"/><rect x="2.6" y="3.4" width="4.8" height="3.4" fill="#0a3d80"/></svg>office@summitshield.example</li>
      <li><svg viewBox="0 0 10 10"><circle cx="5" cy="5" r="4.5" fill="#fff" opacity=".8"/><path d="M1 5 H9 M5 1 V9" stroke="#0a3d80" stroke-width=".8"/></svg>summitshieldinsulation.example</li>
    </ul>
    <nav class="services">SPRAY FOAM<span class="sep">|</span>FIBERGLASS<span class="sep">|</span>INSULATION<span class="sep">|</span>ROOFING</nav>
  </header>

  <article class="content">
    <h2 class="subhead">Subtittle Loremipsum</h2>
    <p>Lorem ipsum dolor sit amet, consectetur adipiscing elit. Praesent ut lobortis est, at laoreet leo. Aliquam posuere placerat elementum. Pellentesque et ornare risus. Vestibulum blandit arcu nisi, elementum blandit elit facilisis a. Duis molestie malesuada condimentum. Proin auctor blandit diam vestibulum dapibus. Proin laoreet pellentesque felis, at fermentum neque sagittis ut. Duis gravida est vitae purus mollis laoreet.</p>
    <p>Pellentesque sagittis auctor sapien, vel rhoncus libero commodo et. Nullam in imperdiet ligula, eu mollis erat. In hac habitasse platea dictumst. Aliquam ligula mi, posuere vitae sem ut, vestibulum commodo dui. Integer commodo, metus vehicula laoreet interdum, odio felis condimentum metus, in pretium sem risus quis arcu. In eget nisl tempus arcu scelerisque pulvinar et sit amet magna. Lorem ipsum dolor sit amet, consectetur adipiscing elit. Praesent turpis neque, tincidunt vel ante vel, pellentesque porttitor dui. Maecenas pellentesque commodo elit et iaculis.</p>
    <p>Nulla varius eros suscipit, sodales metus at, pretium ipsum. Donec vulputate, justo eget vestibulum fringilla, tellus diam varius dui, ac rhoncus ante velit eu dolor. Vestibulum eget urna in elit dignissim luctus vel et nunc. Proin erat orci, iaculis eget nunc in, hendrerit egestas metus. Duis molestie sagittis metus sed cursus. Curabitur mollis mi et euismod vehicula. Nam tincidunt aliquam nunc a ornare. Suspendisse vestibulum laoreet felis bibendum placerat. Integer quam justo, consequat in erat vel, venenatis auctor magna. Donec a leo ut felis congue dictum. Etiam neque leo, tincidunt id ipsum sit amet, euismod rutrum nunc. Vivamus at libero orci.</p>
    <p>Proin commodo dictum dui. Proin venenatis turpis ac nunc auctor, et suscipit ipsum efficitur. Mauris vulputate neque nec est placerat, ac pharetra metus interdum. Pellentesque vitae nisl semper, vehicula nisi in, gravida massa. Nunc justo ipsum, convallis ut augue in, interdum pretium tortor. Praesent pharetra semper augue ac euismod. Ut non lectus euismod, vehicula ante at, sollicitudin risus. In hac habitasse platea dictumst. In congue elit mi, et dictum risus pulvinar in.</p>
    <p>Integer luctus tellus dui. Nulla eget neque sed massa semper lacinia eu id tortor. Etiam lacinia, nulla sed sodales porttitor, orci quam blandit nulla, nec ultricies ipsum nibh quis</p>
  </article>

  <div class="footer-band"></div>
</section>

</body>
</html>
```